Homemaker goats milk soap label

The name of my farm is Fern N Heron Farm. I would like to keep my label vintage 1800s is appearance. A linked to my webpage, still under development is http://lopo.mivtrel.com/dev2/pastureway/. This will give you a feel for my theme. Along with other goat and bison by products, I make and sell homemade goat milk soap and I would like a special label to package my fabulous soap.
Updates

Hello Designers, To assist you with designing my label, I have attached a new photo from Lather Harbor that shows the type label I am going to use.

Industry/Entity Type

Farm

```html
<!DOCTYPE html>
<html lang="en">
<head>
<meta charset="utf-8">
<title>Fern N Heron Goats Milk Soap Label</title>
<link rel="stylesheet" href="https://fonts.googleapis.com/css2?family=Alice&family=IM+Fell+Double+Pica&display=swap">
<style>
  :root {
    --canvas: #ffffff;
    --label-base: #fdf7ab;
    --stripe: #e4cd90;
    --ink: #a88a5c;
    --art-fill: #eadb9c;
  }
  html, body { margin: 0; padding: 0; overflow: hidden; }
  body { width: 1200px; height: 1001px; background: var(--canvas); position: relative; }
  .label {
    position: absolute; left: 3px; top: 270px; width: 1197px; height: 464px;
    background: var(--label-base); overflow: hidden;
  }
  .label__stripes {
    position: absolute; inset: 0;
    background:
      linear-gradient(180deg, rgba(253,247,171,.75) 0%, rgba(253,247,171,.35) 35%, rgba(253,247,171,0) 70%),
      repeating-linear-gradient(90deg, transparent 0 31px, var(--stripe) 31px 61px);
  }
  .dot-row {
    position: absolute; height: 10px;
    background: radial-gradient(circle, var(--ink) 4.3px, transparent 4.8px) 0 0 / 13.1px 10px repeat-x;
  }
  .star-row { position: absolute; }
  .star-row svg { display: block; }
  .title-home, .title-brand, .title-product, .ingredients, .net-weight {
    position: absolute; margin: 0; color: var(--ink); white-space: nowrap; line-height: 1;
  }
  .title-home { left: 270px; top: 14px; font: 39px "Alice", serif; }
  .title-brand { left: 268px; top: 66px; font: 58px "IM Fell Double Pica", serif; letter-spacing: -1px; }
  .title-product { left: 367px; top: 140px; font: 41px "Alice", serif; }
  .ingredients { left: 829px; top: 157px; font: 17px "Alice", serif; }
  .net-weight { left: 799px; top: 426px; font: 29px "Alice", serif; font-weight: 700; }
  .scent-badge { position: absolute; left: 262px; top: 145px; }
  .artwork { position: absolute; left: 252px; top: 195px; }
</style>
</head>
<body>
  <div class="label">
    <div class="label__stripes"></div>

    <div class="dot-row" style="left:7px;top:48px;width:214px"></div>
    <div class="dot-row" style="left:7px;top:129px;width:214px"></div>
    <div class="dot-row" style="left:7px;top:324px;width:214px"></div>
    <div class="dot-row" style="left:7px;top:405px;width:214px"></div>
    <div class="dot-row" style="left:673px;top:48px;width:490px"></div>
    <div class="dot-row" style="left:673px;top:129px;width:490px"></div>
    <div class="dot-row" style="left:673px;top:324px;width:490px"></div>
    <div class="dot-row" style="left:673px;top:405px;width:490px"></div>

    <svg width="0" height="0" style="position:absolute">
      <defs>
        <polygon id="star" points="0,-21 4.9,-6.7 20,-6.5 7.9,2.5 12.3,17 0,8.3 -12.3,17 -7.9,2.5 -20,-6.5 -4.9,-6.7" fill="#a88a5c"/>
      </defs>
    </svg>
    <svg class="star-row" style="left:0;top:72px" width="1197" height="44">
      <use href="#star" x="9" y="23"/><use href="#star" x="81" y="23"/><use href="#star" x="155" y="23"/>
      <use href="#star" x="725" y="23"/><use href="#star" x="799" y="23"/><use href="#star" x="873" y="23"/>
      <use href="#star" x="947" y="23"/><use href="#star" x="1021" y="23"/><use href="#star" x="1095" y="23"/>
    </svg>
    <svg class="star-row" style="left:0;top:348px" width="1197" height="44">
      <use href="#star" x="9" y="23"/><use href="#star" x="81" y="23"/><use href="#star" x="155" y="23"/>
      <use href="#star" x="725" y="23"/><use href="#star" x="799" y="23"/><use href="#star" x="873" y="23"/>
      <use href="#star" x="947" y="23"/><use href="#star" x="1021" y="23"/><use href="#star" x="1095" y="23"/>
    </svg>

    <p class="title-home">Home Crafted</p>
    <h1 class="title-brand">Fern N Heron</h1>
    <p class="title-product">Goats Milk Soap</p>

    <svg class="artwork" width="386" height="260" role="img" aria-label="Illustration of a goat and a bison head facing each other inside an oval frame">
      <ellipse cx="193" cy="128" rx="188" ry="124" fill="var(--art-fill)" stroke="#c9ad78" stroke-width="4"/>
    </svg>

    <svg class="scent-badge" width="118" height="90">
      <circle cx="58" cy="44" r="42" fill="#a88a5c"/>
      <text x="58" y="52" text-anchor="middle" transform="rotate(-18 58 48)" font-family="Alice, serif" font-size="24" fill="#fdf7ab">vanilla</text>
    </svg>

    <p class="ingredients">Ingredients:</p>
    <p class="net-weight">nett. weight 4.5 oz</p>
  </div>
</body>
</html>
```